wine bottle label design

My girlfriend and I are getting married. We are sending out invitations, in a wine bottle. For that we need a label on the bottle.
Our names are Marlene & Henrik. We would like the C and K to somehow play a bigger part in the logo.
Also maybe with an Illustration (best if made as a drawing resembling the church we are getting married in) https://www.sangfolket.dk/index.php/kalender/83-uncategorised/148-gospelgudstjeneste-i-tarnholm-kirke.html

Logo Text

Bryllup den 27 april 2019, kl. 14:00 i Tarnholm Kirke

Font styles to use
Decorative

```html
<!DOCTYPE html>
<html lang="da">
<head>
<meta charset="utf-8">
<title>Henrik &amp; Marlene – Vinetiket</title>
<link rel="stylesheet" href="https://fonts.googleapis.com/css2?family=Dancing+Script:wght@500;600&family=Cormorant+Garamond:wght@500&display=swap">
<style>
  :root {
    --backdrop: #ebe8ea;
    --label-white: #ffffff;
    --gold: #d6a24c;
    --gold-light: #ecd2a0;
    --gold-pale: #f7ecd8;
    --copper: #cd8438;
    --ink-grey: #8c8c8e;
  }
  html, body {
    margin: 0;
    padding: 0;
    width: 694px;
    height: 1200px;
    overflow: hidden;
    background: var(--backdrop);
  }
  .canvas {
    position: relative;
    width: 694px;
    height: 1200px;
  }
  .label {
    position: absolute;
    left: 37px;
    top: 231px;
    width: 620px;
    height: 738px;
    background: var(--label-white);
    overflow: hidden;
    box-shadow: 0 2px 8px rgba(0,0,0,0.08);
  }
  .floral-pattern {
    position: absolute;
    inset: 0;
    background:
      radial-gradient(circle at 20% 30%, var(--gold-pale), transparent 60%),
      radial-gradient(circle at 80% 75%, var(--gold-pale), transparent 60%),
      linear-gradient(135deg, #fbf3e4, #f3e1bf 50%, #fbf3e4);
  }
  .name-frame {
    position: absolute;
    left: 97px;
    top: 88px;
    width: 433px;
    height: 544px;
    box-sizing: border-box;
    background: var(--label-white);
    border: 5px solid var(--gold);
    box-shadow: inset 0 0 0 1px var(--gold-light);
    overflow: hidden;
  }
  .couple-names {
    position: absolute;
    left: 0;
    right: 0;
    top: 20px;
    margin: 0;
    text-align: center;
    font-family: "Dancing Script", cursive;
    font-weight: 500;
    color: var(--ink-grey);
    line-height: 1;
  }
  .couple-names .name {
    display: block;
    font-size: 62px;
  }
  .couple-names .initial {
    color: var(--copper);
    font-size: 100px;
    font-weight: 600;
  }
  .couple-names .name-first { margin-left: -10px; }
  .couple-names .ampersand {
    display: block;
    color: var(--copper);
    font-size: 44px;
    margin: 4px 0 -6px -40px;
  }
  .couple-names .name-second { margin-left: 10px; }
  .wedding-details {
    position: absolute;
    right: 30px;
    top: 300px;
    margin: 0;
    text-align: right;
    font-family: "Cormorant Garamond", serif;
    font-weight: 500;
    font-size: 19px;
    line-height: 36px;
    letter-spacing: 0.03em;
    color: var(--ink-grey);
  }
  .church-illustration {
    position: absolute;
    left: 8px;
    top: 420px;
    width: 215px;
    height: 106px;
    background: linear-gradient(180deg, rgba(214,162,76,0.25), rgba(205,132,56,0.6));
    border-radius: 40% 40% 4px 4px / 35% 35% 4px 4px;
  }
</style>
</head>
<body>
  <main class="canvas">
    <section class="label">
      <div class="floral-pattern" role="img" aria-label="Gyldent blomster- og bladmønster over hele etiketten"></div>
      <div class="name-frame">
        <h1 class="couple-names">
          <span class="name name-first"><span class="initial">H</span>enrik</span>
          <span class="ampersand">&amp;</span>
          <span class="name name-second"><span class="initial">M</span>arlene</span>
        </h1>
        <p class="wedding-details">BRYLLUP DEN<br>27 APRIL 2019,<br>KL. 14:00 I TARNHOLM KIRKE</p>
        <div class="church-illustration" role="img" aria-label="Gylden tegning af Tarnholm Kirke med tårn på en bakke"></div>
      </div>
    </section>
  </main>
</body>
</html>
```